Velmora and Co Business Card Design

Looking for a business card design. Wanting Smart, Clean and Sharp looking to promote Velmora and Co, our Import Export Business - like Black, White and natural textures. I have uploaded our logo. I like a rounded font but open to other ideas
Being that we have a wide range of products on offer we are looking for a neutral yet eye catching card. We would also like to have Import - Export on the business card to be clear on want our business does.

Target Market(s)

Import export market

Industry/Entity Type

Importer

Contact Information for Business Card

Mr Tobias Kernwell
tobias.kernwell@velmoraandco.com.au
+61 (0) 417 630 284
www.velmoraandco.com.au

Font styles to use
Other font styles liked:
• Unsure of actual font name but something rounded and clean

Colors

Designer to choose colors to be used in the design.

Requirements
Must have
• Instagram icon
• Facebook icon

```html
<!DOCTYPE html>
<html lang="en">
<head>
<meta charset="utf-8">
<title>Velmora and Co Business Card</title>
<link href="https://fonts.googleapis.com/css2?family=Nunito:wght@400;700;800&display=swap" rel="stylesheet">
<style>
  :root {
    --page: #f4f4f4;
    --card: #231f20;
    --ink: #ffffff;
    --ink-soft: #e9e9e9;
    --shadow: rgba(0, 0, 0, 0.35);
  }
  * { margin: 0; padding: 0; box-sizing: border-box; }
  html, body {
    width: 1200px; height: 900px; overflow: hidden;
    background: var(--page);
    font-family: "Nunito", sans-serif;
    color: var(--ink);
  }
  .stage { position: relative; width: 1200px; height: 900px; }
  .card {
    position: absolute;
    background: var(--card);
    border-radius: 20px;
    box-shadow: -4px 6px 10px var(--shadow);
  }
  .card--front { left: 290px; top: 76px; width: 620px; height: 354px; }
  .card--back { left: 287px; top: 468px; width: 624px; height: 356px; }

  .front-brand {
    position: absolute; left: 0; right: 0; top: 140px;
    display: flex; align-items: center; justify-content: center; gap: 14px;
  }
  .brand-square { width: 26px; height: 26px; background: var(--ink); }
  .brand-name { font-weight: 800; font-size: 36px; letter-spacing: 0.5px; color: var(--ink); }
  .front-tagline {
    position: absolute; left: 0; right: 0; top: 270px;
    text-align: center; font-size: 16px; letter-spacing: 2.4px; color: var(--ink);
  }

  .back-brand {
    position: absolute; left: 78px; top: 98px; width: 143px; height: 140px;
    display: flex; align-items: center; gap: 10px;
  }
  .back-brand .brand-square { width: 18px; height: 18px; flex: none; }
  .back-brand .brand-name { font-size: 28px; line-height: 1.05; }
  .follow {
    position: absolute; left: 77px; top: 244px;
    display: flex; align-items: center; gap: 11px; font-size: 16px; color: var(--ink-soft);
  }
  .social-slot { width: 17px; height: 17px; border-radius: 3px; background: var(--ink-soft); }

  .contact { position: absolute; left: 276px; top: 108px; }
  .contact-name { font-size: 19px; letter-spacing: 0.3px; }
  .contact-name strong { font-weight: 800; }
  .contact-role { font-size: 15px; color: var(--ink-soft); margin-top: -1px; }
  .contact-list { list-style: none; margin-top: 13px; }
  .contact-list li {
    display: flex; align-items: center; gap: 9px;
    font-size: 16px; height: 27.5px; color: var(--ink-soft);
  }
  .contact-list svg { width: 19px; height: 19px; fill: var(--ink); flex: none; }
</style>
</head>
<body>
<main class="stage">

  <section class="card card--front" aria-label="Card front">
    <div class="front-brand">
      <span class="brand-square"></span>
      <span class="brand-name">Velmora and Co</span>
    </div>
    <p class="front-tagline">IMPORT &amp; EXPORT</p>
  </section>

  <section class="card card--back" aria-label="Card back">
    <div class="back-brand">
      <span class="brand-square"></span>
      <span class="brand-name">Velmora<br>and Co</span>
    </div>
    <div class="follow">
      <span>Follow Us -</span>
      <span class="social-slot" role="img" aria-label="Social media link"></span>
      <span class="social-slot" role="img" aria-label="Photo sharing link"></span>
    </div>

    <div class="contact">
      <p class="contact-name">Mr TOBIAS <strong>KERNWELL</strong></p>
      <p class="contact-role">CEO | Founder</p>
      <ul class="contact-list">
        <li>
          <svg viewBox="0 0 24 24" aria-hidden="true"><path d="M6.6 10.8c1.4 2.8 3.8 5.1 6.6 6.6l2.2-2.2c.3-.3.7-.4 1-.2 1.1.4 2.3.6 3.6.6.6 0 1 .4 1 1V20c0 .6-.4 1-1 1C10.6 21 3 13.4 3 4c0-.6.4-1 1-1h3.5c.6 0 1 .4 1 1 0 1.3.2 2.5.6 3.6.1.3 0 .7-.2 1z"/></svg>
          <span>+61 (0) 417 630 284</span>
        </li>
        <li>
          <svg viewBox="0 0 24 24" aria-hidden="true"><path d="M2 6.5C2 5.7 2.7 5 3.5 5h17c.8 0 1.5.7 1.5 1.5v.3l-10 6.4-10-6.4z"/><path d="M2 9.2l10 6.3 10-6.3v8.3c0 .8-.7 1.5-1.5 1.5h-17c-.8 0-1.5-.7-1.5-1.5z"/></svg>
          <span>tobias.kernwell@velmoraandco.com.au</span>
        </li>
        <li>
          <svg viewBox="0 0 24 24" aria-hidden="true"><path d="M12 2a10 10 0 1 0 0 20 10 10 0 0 0 0-20zm-1 17.9A8 8 0 0 1 4.2 10.2L9 15v1c0 1.1.9 2 2 2zm6.9-2.5c-.3-.8-1-1.4-1.9-1.4h-1v-3c0-.6-.4-1-1-1H8v-2h2c.6 0 1-.4 1-1V7h2c1.1 0 2-.9 2-2v-.4a8 8 0 0 1 2.9 12.8z"/></svg>
          <span>www.velmoraandco.com.au</span>
        </li>
      </ul>
    </div>
  </section>

</main>
</body>
</html>
```